Modern Design Business Card industrial maintenance company

Business card design for Company named Brookvale Equipment Services

Target Market(s)

Industrial

Industry/Entity Type

Maintenance and repair

Contact Information for Business Card

Place holder for address, office phone, mobile number and email

Requirements
Must have
• Clean modern look
Nice to have
• N/a

```html
<!DOCTYPE html>
<html lang="en">
<head>
<meta charset="utf-8">
<title>Brookvale Equipment Services – Business Card</title>
<link rel="stylesheet" href="https://fonts.googleapis.com/css2?family=Montserrat:wght@400;600;700&display=swap">
<style>
  :root {
    --backdrop: #6a6a6a;
    --card: #161616;
    --card-back: #121212;
    --ink: #ffffff;
    --ink-soft: #e6e6e6;
    --emboss: #2c2c2c;
  }
  * { margin: 0; padding: 0; box-sizing: border-box; }
  html, body {
    width: 1200px;
    height: 801px;
    overflow: hidden;
    background: var(--backdrop);
    font-family: "Montserrat", sans-serif;
  }
  .stage {
    position: relative;
    width: 1200px;
    height: 801px;
    display: flex;
    align-items: center;
    justify-content: center;
    gap: 40px;
  }
  .card {
    position: relative;
    width: 540px;
    height: 309px;
    border-radius: 2px;
    box-shadow: 0 14px 30px rgba(0,0,0,.28);
    overflow: hidden;
  }
  .card--front { background: var(--card); color: var(--ink); }
  .card--back { background: var(--card-back); }

  /* front: brand block */
  .brand {
    position: absolute;
    left: 34px;
    top: 0;
    width: 214px;
    height: 100%;
    display: flex;
    flex-direction: column;
    align-items: center;
    justify-content: center;
    gap: 16px;
  }
  .brand__mark {
    width: 74px;
    height: 74px;
    border: 4px solid var(--ink);
    border-radius: 50%;
  }
  .brand__name {
    font-weight: 600;
    font-size: 15px;
    letter-spacing: 2px;
    line-height: 1.45;
    text-align: center;
    text-transform: uppercase;
    color: var(--ink);
  }
  .divider {
    position: absolute;
    left: 270px;
    top: 52px;
    width: 1.5px;
    height: 205px;
    background: var(--ink);
  }

  /* front: contact block */
  .contact {
    position: absolute;
    left: 296px;
    top: 50px;
    width: 230px;
  }
  .contact__name {
    font-weight: 700;
    font-size: 19px;
    letter-spacing: 1px;
    text-transform: uppercase;
  }
  .contact__role {
    font-size: 12.5px;
    margin-top: 2px;
    color: var(--ink-soft);
  }
  .contact__list {
    list-style: none;
    margin-top: 14px;
    font-size: 12.5px;
    color: var(--ink-soft);
  }
  .contact__list li {
    display: flex;
    align-items: center;
    gap: 8px;
    height: 19px;
  }
  .contact__list svg { width: 12px; height: 12px; flex: none; fill: var(--ink); }
  .contact__address {
    margin-top: 10px;
    font-size: 12.5px;
    line-height: 1.5;
    color: var(--ink-soft);
  }

  /* back: tonal brand */
  .back-brand {
    position: absolute;
    inset: 0;
    display: flex;
    flex-direction: column;
    align-items: center;
    justify-content: center;
    gap: 22px;
  }
  .back-brand__mark {
    width: 120px;
    height: 120px;
    border: 6px solid var(--emboss);
    border-radius: 50%;
  }
  .back-brand__name {
    font-weight: 600;
    font-size: 22px;
    letter-spacing: 3px;
    text-transform: uppercase;
    color: var(--emboss);
  }
</style>
</head>
<body>
<main class="stage">
  <section class="card card--front" aria-label="Business card front">
    <div class="brand">
      <div class="brand__mark"></div>
      <p class="brand__name">Brookvale<br>Equipment Services</p>
    </div>
    <div class="divider"></div>
    <div class="contact">
      <h1 class="contact__name">Daniel Hart</h1>
      <p class="contact__role">Managing Director</p>
      <ul class="contact__list">
        <li>
          <svg viewBox="0 0 24 24" aria-hidden="true"><path d="M6.6 10.8a15 15 0 0 0 6.6 6.6l2.2-2.2c.3-.3.7-.4 1-.2 1.1.4 2.3.6 3.6.6.6 0 1 .4 1 1V20c0 .6-.4 1-1 1A17 17 0 0 1 3 4c0-.6.4-1 1-1h3.5c.6 0 1 .4 1 1 0 1.3.2 2.5.6 3.6.1.3 0 .7-.2 1z"/></svg>
          123 456 789
        </li>
        <li>
          <svg viewBox="0 0 24 24" aria-hidden="true"><path d="M7 1h10a2 2 0 0 1 2 2v18a2 2 0 0 1-2 2H7a2 2 0 0 1-2-2V3a2 2 0 0 1 2-2zm0 3v15h10V4zm5 16.2a1 1 0 1 0 0 .1z"/></svg>
          123 456 789
        </li>
        <li>
          <svg viewBox="0 0 24 24" aria-hidden="true"><path d="M2 5h20v14H2zm2 2v.4l8 5.3 8-5.3V7zm0 2.8V17h16V9.8l-8 5.3z"/></svg>
          info@yourgmail.com
        </li>
        <li>
          <svg viewBox="0 0 24 24" aria-hidden="true"><path d="M12 2a10 10 0 1 0 0 20 10 10 0 0 0 0-20zm6.9 6h-3a15 15 0 0 0-1.3-4 8 8 0 0 1 4.3 4zM12 4c.8 1.2 1.5 2.5 1.9 4h-3.8c.4-1.5 1.1-2.8 1.9-4zM4.3 14a8 8 0 0 1 0-4h3.4a16 16 0 0 0 0 4zm.8 2h3a15 15 0 0 0 1.3 4 8 8 0 0 1-4.3-4zm3-8h-3a8 8 0 0 1 4.3-4 15 15 0 0 0-1.3 4zM12 20c-.8-1.2-1.5-2.5-1.9-4h3.8c-.4 1.5-1.1 2.8-1.9 4zm2.3-6H9.7a14 14 0 0 1 0-4h4.6a14 14 0 0 1 0 4zm.3 6a15 15 0 0 0 1.3-4h3a8 8 0 0 1-4.3 4zm1.7-6a16 16 0 0 0 0-4h3.4a8 8 0 0 1 0 4z"/></svg>
          www.yourwebsite.com
        </li>
      </ul>
      <p class="contact__address">Your address, City<br>State, Zip 1234</p>
    </div>
  </section>

  <section class="card card--back" aria-label="Business card back">
    <div class="back-brand">
      <div class="back-brand__mark"></div>
      <p class="back-brand__name">Brookvale Equipment Services</p>
    </div>
  </section>
</main>
</body>
</html>
```